Werbebanner für Netzwerk-Werbung
Zielgruppe
Alle - also Business und Privat, da wir Messen aus allen Bereichen und Kategorien bzw. zu jedem Thema anbieten, gibt es für diese Banner keine spezielle, eingeschränkte Zielgruppe.
Aufgabenstellung
Wir benötigen insgesamt 3 Werbebanner (vorzugsweise Flash) in folgenden Größen:
1. 300x250
2. 728x90
3. 160x600
Die Banner müssen grundsätzlich seriös sein und zu unserer Webseite www.tribolux.de passen.
Wir haben kein Problem damit, wenn "provokannte" Vorschläge kommen.
Da die Banner für Netzwerk-Werbung, also Reichweite/Masse gedacht sind, müssen sie in jedem Fall auffällig sein und direkt ins Auge stechen.
Die Banner-Farbe muss nicht zwingend blau sein, sollte jedoch zum Logo bzw. Style von Tribolux.de passen (Wiedererkennungswert).
Auf den Bannern sollten keine Länder, Regionen oder ähnliches erwähnt werden.

```html
<!DOCTYPE html>
<html lang="de">
<head>
<meta charset="utf-8">
<title>Tribolux.de – Bannerablauf Szenen 1–4</title>
<link rel="stylesheet" href="https://fonts.googleapis.com/css2?family=Questrial&display=swap">
<style>
:root{
  --bg:#000;
  --glow:#1e6fd0;
  --glow-soft:rgba(30,111,208,.35);
  --panel:#1f5a96;
  --frame:#ffffff;
  --screen:#050505;
  --cyan:#1aa3f0;
  --cyan-light:#2fd2f0;
  --white:#ffffff;
  --magenta:#e020c8;
  --box-top:#2f6ea8;
  --box-bottom:#174a80;
  --label-bg:#0b1624;
  --green:#39c24a;
  --ink:#1c1c1c;
}
*{margin:0;padding:0;box-sizing:border-box}
html,body{width:1200px;height:1200px;overflow:hidden;background:var(--bg)}
body{font-family:"Questrial",sans-serif;position:relative}
.light-column{position:absolute;left:300px;top:0;width:645px;height:1200px;
  background:linear-gradient(90deg,var(--glow) 0%,rgba(20,70,140,.55) 3%,rgba(8,25,55,.6) 15%,rgba(8,25,55,.6) 85%,rgba(20,70,140,.55) 97%,var(--glow) 100%);
  box-shadow:0 0 40px var(--glow-soft)}
.board{position:absolute;left:444px;top:52px;width:354px;height:1084px;background:var(--panel)}
.scene{position:absolute;left:484px;width:262px;background:var(--frame);padding:10px}
.screen{width:100%;height:100%;background:var(--screen);position:relative;overflow:hidden;
  display:flex;flex-direction:column;align-items:center;justify-content:center;text-align:center}
.s1{top:102px;height:225px}
.s2{top:355px;height:224px}
.s3{top:606px;height:224px}
.s4{top:861px;height:222px}
.spot{position:absolute;left:30px;top:20px;width:150px;height:140px;border-radius:50%;
  background:radial-gradient(circle,#3a3a3a 0%,#1a1a1a 45%,rgba(5,5,5,0) 75%)}
.s3 .spot{left:40px;top:15px;width:170px;height:160px}
.headline{font-size:35px;line-height:1.2;color:var(--cyan)}
.headline .em{color:var(--white);font-size:38px}
.teaser{position:relative;font-size:21px;color:var(--cyan-light);line-height:1}
.teaser-sub{position:relative;font-size:16px;color:var(--white);margin-top:2px}
.teaser-note{position:relative;font-size:8.5px;color:var(--magenta);margin-top:8px}
.s4 .screen{background:var(--frame);justify-content:flex-start;gap:6px}
.offer{width:100%;height:105px;background:linear-gradient(180deg,var(--box-top),var(--box-bottom));
  border:2px solid #0e3560;padding:6px 8px;color:var(--white);text-align:center}
.offer-quote{font-size:10px;color:#bfe4ff}
.offer-title{font-size:18px;margin-top:3px}
.offer-sub{font-size:11px;color:var(--cyan-light)}
.offer-check{display:flex;align-items:center;gap:6px;font-size:13px;margin:8px 0 0 10px}
.brand{width:100%;flex:1;border:1px solid #ccc;display:flex;flex-direction:column;justify-content:center;padding:0 10px}
.brand-name{font-size:30px;color:var(--ink);text-align:left}
.brand-claim{font-size:8px;color:var(--ink);text-align:right;margin-top:6px}
.scene-label{position:absolute;left:278px;width:134px;height:33px;background:var(--label-bg);
  border:2px solid #6fb4ff;border-radius:3px;box-shadow:0 0 10px var(--glow),0 0 22px var(--glow);
  color:var(--white);font-size:20px;display:flex;align-items:center;justify-content:center;letter-spacing:.5px}
.l1{top:204px}.l2{top:456px}.l3{top:706px}.l4{top:963px}
</style>
</head>
<body>
<div class="light-column"></div>
<div class="board"></div>

<section class="scene s1">
  <div class="screen"><div class="spot" role="img" aria-label="Schwach beleuchteter Lichtkegel auf dunklem Grund"></div></div>
</section>

<section class="scene s2">
  <div class="screen">
    <p class="headline">"Tappen Sie<br>noch im<br><span class="em">Dunkeln?"</span></p>
  </div>
</section>

<section class="scene s3">
  <div class="screen">
    <div class="spot" role="img" aria-label="Schwach beleuchteter Lichtkegel auf dunklem Grund"></div>
    <p class="teaser">" ... oder haben Sie</p>
    <p class="teaser-sub">schon was gefunden ?"</p>
    <p class="teaser-note">Fischbrötchen Ausstellung am kleinen Dorfteich?!</p>
  </div>
</section>

<section class="scene s4">
  <div class="screen">
    <div class="offer">
      <p class="offer-quote">" Kommen Sie doch gleich zu uns "</p>
      <p class="offer-title">Bei uns finden Sie alles</p>
      <p class="offer-sub">... rund ums Thema Messen</p>
      <p class="offer-check">
        <svg width="16" height="16" viewBox="0 0 16 16" aria-hidden="true"><circle cx="8" cy="8" r="7" fill="#fff"/><path d="M4 8.5l3 3 5-7" stroke="var(--green)" stroke-width="2.4" fill="none" stroke-linecap="round"/></svg>
        Alle Städte
      </p>
    </div>
    <div class="brand">
      <p class="brand-name">Tribolux.de</p>
      <p class="brand-claim">die Adresse rund um die Messe...</p>
    </div>
  </div>
</section>

<div class="scene-label l1">SZENE 1</div>
<div class="scene-label l2">SZENE 2</div>
<div class="scene-label l3">SZENE 3</div>
<div class="scene-label l4">SZENE 4</div>
</body>
</html>
```